Book Cover needed for Printed Book entitled "Step 7"

The Book's Title is "Step 7", the sub-title is "One Resident's Manual on Calm Roadside Stops by Patrol Units", and the author is "Desmond Okafor". The front cover may have just the Title, or it may have a combination of the Title, Sub-Title, and Author. We would like to see designs that presents a feeling of peace and cooperation between US Police Officers and Civilians. The cover can include photographs, illustrations, or just words. But the cover should make the viewer want to open the book for more information.

Target Market(s)

Young adults who live in US inner-cities between ages 18 to 30.

Font styles to use
Sans Serif

Colors

Designer to choose colors to be used in the design.

Requirements
Must have
• Most US Police Officers use the phrase "STEP 7" to tell other officers that the situation is under control and no assistance is needed. And the book will teach Civilians how to safely conduct themselves during police encounters - which will end with the Cops calling in "STEP 7" to the dispatcher. So, the front cover must have the phrase "STEP 7" in big bold letters.
Nice to have
• We would like to see designs that present a feeling of peace and cooperation between US Police Officers and Civilians. Pictures and illustrations of people are acceptable but is not required.

```html
<!DOCTYPE html>
<html lang="en">
<head>
<meta charset="utf-8">
<title>Step 7 — Desmond Okafor</title>
<link rel="stylesheet" href="https://fonts.googleapis.com/css2?family=Anton&family=Bebas+Neue&family=Oswald:wght@600&display=swap">
<style>
  :root {
    --sky-top: #2f6fcf;
    --sky-mid: #7fb0e6;
    --sky-low: #dde9f6;
    --flag-navy: #1c2547;
    --flag-red: #c8202b;
    --flag-white: #f2f2f2;
    --subtitle: #ffffff;
    --subtitle-shadow: #1d1d22;
    --author: #d8202b;
  }
  html, body {
    margin: 0;
    padding: 0;
    overflow: hidden;
    background: #ffffff;
  }
  .cover {
    position: relative;
    width: 799px;
    height: 1200px;
    overflow: hidden;
  }
  .sky-backdrop {
    position: absolute;
    inset: 0;
    background: linear-gradient(180deg, var(--sky-top) 0%, var(--sky-mid) 45%, var(--sky-low) 100%);
  }
  .title-art {
    position: absolute;
    inset: 0;
    width: 799px;
    height: 1200px;
  }
  .subtitle {
    position: absolute;
    left: 408px;
    top: 428px;
    margin: 0;
    font-family: "Bebas Neue", "Oswald", sans-serif;
    font-weight: 400;
    font-size: 74px;
    line-height: 84px;
    color: var(--subtitle);
    text-transform: uppercase;
    text-shadow: 3px 3px 0 var(--subtitle-shadow);
    letter-spacing: 0;
  }
  .subtitle span { display: block; white-space: nowrap; }
  .author {
    position: absolute;
    right: 34px;
    top: 950px;
    margin: 0;
    font-family: "Oswald", sans-serif;
    font-weight: 600;
    font-size: 40px;
    letter-spacing: 1px;
    color: var(--author);
  }
</style>
</head>
<body>
<main class="cover">
  <div class="sky-backdrop" role="img" aria-label="Clear blue sky fading to white"></div>

  <svg class="title-art" viewBox="0 0 799 1200" role="img" aria-label="Title STEP 7 in huge letters filled with a waving American flag">
    <defs>
      <linearGradient id="flag-fill" x1="0" y1="0" x2="1" y2="1">
        <stop offset="0" stop-color="var(--flag-navy)"/>
        <stop offset="0.45" stop-color="var(--flag-navy)"/>
        <stop offset="0.62" stop-color="var(--flag-red)"/>
        <stop offset="0.8" stop-color="var(--flag-white)"/>
        <stop offset="1" stop-color="var(--flag-red)"/>
      </linearGradient>
    </defs>
    <text class="title-word" x="0" y="400" textLength="799" lengthAdjust="spacingAndGlyphs"
          font-family="Anton, sans-serif" font-size="545" fill="url(#flag-fill)">STEP</text>
    <text class="title-number" x="0" y="1200" textLength="464" lengthAdjust="spacingAndGlyphs"
          font-family="Anton, sans-serif" font-size="1100" fill="url(#flag-fill)">7</text>
  </svg>

  <h2 class="subtitle">
    <span>One Resident's</span>
    <span>Manual on</span>
    <span>Calm</span>
    <span>Roadside</span>
    <span>Stops by</span>
    <span>Patrol Units</span>
  </h2>

  <p class="author">Desmond Okafor</p>
</main>
</body>
</html>
```